Campaign Flyer for a local election

Black and white election flyer

See information below to be included:

Re-elect Dorian
Experienced Willows Board Member
Experienced NYC Principal
Experienced leader

One Year Board Accomplishments:
-Installed New Park Lights (Bollards)
-Red Brick Road Repair Project
-Established Closer Ties with Our local precinct to frequently monitor the community with directed security patrols. Requested an increased police presence.
-Met with the 62nd Precinct Officials & Assemblywoman, Marla Quintrell to discuss our security issues
- Focused on maintenance of streetlights to make brighter streets
-Negotiated Contract & Hired Our New Landscaper, Oakhollow Landscapers
-Major Homeowner Shrub Replacement Project
- Addressing Standing Water in our Park (Installed French Drain)
- Replaced and upgraded all 5 outdoor circuit breaker panels
-Write monthly community newsletters
-Sewer cleaning project (had all community catch basins cleaned)
-Carefully overseeing our new school project. Coordinating with the sponsor and the school directors
-Delivered a very healthy budget to the community
-Works closely with our committees
-Events: Zoo event, Petting Zoo, Outdoor Movie Night, Egg Hunt

It is my intent to seek re-election.
(Photo) Dorian Lindqvist
-Dedicated to improving our community
-Hard-working…He gets thing done!
-Trustworthy

. .

Please note, I am submitting new information under accomplishments. The list of accomplishments should be in the same sequence, starting with: Met with the 62nd Precinct....
Please carefully review.
----------------------------------------------------------------------------------------------------------------------------------------------------------------

Re-elect Dorian
Experienced NYC Principal
Experienced leader

Last Year’s Board Accomplishments:

-Met with the 62nd Precinct Officials & Assemblywoman, Marla Quintrell, to discuss our security issues. Requested increased police presence.
-Established a strong partnership with the 62nd precinct to frequently monitor the community with directed security patrols.
-Replaced all new park lights (Bollards) to make the park brighter
- Focused on maintenance of streetlights to make streets brighter
-‘Fixing Our Streets Project’ (Repaired all cracked/missing red bricks)
-Homeowner Shrub Replacement Project (Replaced hundreds of bushes)
- I write the monthly community newsletter
-Carefully overseeing our new school project. Coordinating with the sponsor and the school director
-Monitoring C of O’s and homeowners Insurance

(Photo) Dorian Lindqvist
-Hard-working! I get things done!
-Trustworthy

. .

Re-elect Dorian
Experienced NYC Principal
Experienced leader

(Photo) Dorian Lindqvist
-Trustworthy

. .

Target Market(s)

A Community electing a Board Member

Industry/Entity Type

residential election

Requirements
Must have
• all black, white and grey print. Flyers will not be printed in color
Nice to have
• See the information in the attachment below containing all my accomplishments
Should not have
• color

```html
<!DOCTYPE html>
<html lang="en">
<head>
<meta charset="utf-8">
<title>Re-elect Dorian – Campaign Flyer</title>
<link rel="stylesheet" href="https://fonts.googleapis.com/css2?family=Anton&family=Oswald:wght@500&family=Barlow+Condensed:ital,wght@1,400;1,600&display=swap">
<style>
  :root {
    --ink: #111111;
    --paper: #ffffff;
    --backdrop: #5a5a5a;
    --rule: #222222;
    --photo-light: #d6d6d6;
    --photo-mid: #a6a6a6;
    --photo-dark: #7c7c7c;
  }
  * { margin: 0; padding: 0; box-sizing: border-box; }
  html, body { width: 1200px; height: 800px; overflow: hidden; }
  body {
    background: var(--backdrop);
    position: relative;
    font-family: "Barlow Condensed", "Arial Narrow", sans-serif;
    color: var(--ink);
  }
  .flyer {
    position: absolute;
    left: 318px; top: 27px;
    width: 568px; height: 735px;
    background: var(--paper);
    overflow: hidden;
  }
  .masthead {
    position: absolute; left: 0; top: 0;
    width: 100%; height: 99px;
    background: var(--ink);
    color: var(--paper);
    font-family: "Anton", sans-serif; font-weight: 400;
    font-size: 74px; line-height: 99px;
    text-align: center;
    letter-spacing: 0.5px;
  }
  .credentials-mark {
    position: absolute; left: 94px; top: 104px;
    width: 84px; height: 80px;
  }
  .credentials {
    position: absolute; left: 179px; top: 107px;
    list-style: none;
    font-family: "Oswald", sans-serif; font-weight: 500;
    font-size: 19px; line-height: 25px;
  }
  .credentials strong { font-family: "Anton", sans-serif; font-weight: 400; letter-spacing: 0.3px; }
  .accomplishments {
    position: absolute; left: 28px; top: 206px;
    width: 511px; height: 328px;
    border: 1.5px solid var(--rule);
    border-radius: 6px;
  }
  .accomplishments-title {
    position: absolute; left: 64px; top: 191px;
    width: 440px; height: 34px;
    background: var(--ink); color: var(--paper);
    font-family: "Anton", sans-serif; font-weight: 400;
    font-size: 30px; line-height: 34px;
    text-align: center;
  }
  .portrait {
    position: absolute; left: 210px; top: 455px;
    width: 358px; height: 280px;
    background: linear-gradient(to right, var(--paper) 0%, var(--photo-light) 30%, var(--photo-mid) 58%, var(--photo-dark) 100%);
    clip-path: polygon(208px 0, 358px 0, 358px 280px, 0 280px, 0 85px, 208px 85px);
    z-index: 0;
  }
  .achievements {
    position: absolute; left: 0; top: 0;
    width: 100%; height: 100%;
    list-style: none;
    font-style: italic; font-weight: 400;
    font-size: 13.5px; line-height: 17px;
    letter-spacing: -0.1px;
    z-index: 1;
  }
  .achievements li {
    position: absolute;
    white-space: nowrap;
    padding-left: 14px;
  }
  .achievements .col-left { left: 44px; }
  .achievements .col-right { left: 293px; }
  .tick {
    position: absolute; left: 0; top: 2px;
    width: 12px; height: 12px;
  }
  .achievements .event-line { left: 91px; }
  .achievements .event-line strong { font-weight: 600; }
  .intent, .candidate-name, .qualities { position: absolute; left: 25px; z-index: 1; }
  .intent {
    top: 540px;
    font-family: "Anton", sans-serif; font-weight: 400;
    font-size: 27px; line-height: 36px;
  }
  .candidate-name {
    top: 577px;
    font-family: "Anton", sans-serif; font-weight: 400;
    font-size: 56px; line-height: 60px;
    letter-spacing: -0.3px;
  }
  .qualities {
    top: 637px;
    list-style: none;
    font-family: "Oswald", sans-serif; font-weight: 500;
    font-size: 19.5px; line-height: 27px;
  }
  .qualities li::before {
    content: "";
    display: inline-block;
    width: 7px; height: 7px;
    border-radius: 50%;
    background: var(--ink);
    margin: 0 6px 4px 2px;
    vertical-align: middle;
  }
</style>
</head>
<body>
<svg width="0" height="0" style="position:absolute">
  <defs>
    <symbol id="tick" viewBox="0 0 20 20">
      <circle cx="10" cy="10" r="8.3" fill="none" stroke="#111" stroke-width="2"/>
      <path d="M5.5 10.5 L9 14 L19 3" fill="none" stroke="#111" stroke-width="2.8" stroke-linecap="round" stroke-linejoin="round"/>
    </symbol>
  </defs>
</svg>

<main class="flyer">
  <h1 class="masthead">Re-elect DORIAN</h1>

  <svg class="credentials-mark" viewBox="0 0 84 80" aria-hidden="true">
    <rect x="3" y="15" width="60" height="60" rx="6" fill="none" stroke="#111" stroke-width="5"/>
    <path d="M16 42 L31 58 L80 4" fill="none" stroke="#111" stroke-width="10" stroke-linecap="round" stroke-linejoin="round"/>
  </svg>
  <ul class="credentials">
    <li>Experienced <strong>WILLOWS BOARD MEMBER</strong></li>
    <li>Experienced <strong>NYC PRINCIPAL</strong></li>
    <li>Experienced <strong>LEADER</strong></li>
  </ul>

  <section class="accomplishments" aria-label="One Year Board Accomplishments"></section>
  <h2 class="accomplishments-title">One Year Board Accomplishments:</h2>

  <div class="portrait" role="img" aria-label="Portrait photo of candidate Dorian Lindqvist in front of a grassy dune landscape"></div>

  <ul class="achievements">
    <li class="col-left" style="top:233px"><svg class="tick"><use href="#tick"/></svg>Installed New Park Lights (Bollards)</li>
    <li class="col-left" style="top:254.5px"><svg class="tick"><use href="#tick"/></svg>Red Brick Road Repair Project</li>
    <li class="col-left" style="top:277px"><svg class="tick"><use href="#tick"/></svg>Established Closer Ties with Our local precinct<br>to frequently monitor the community with<br>directed security patrols. Requested an<br>increased police presence.</li>
    <li class="col-left" style="top:349px"><svg class="tick"><use href="#tick"/></svg>Met with the 62nd Precinct Officials &amp;<br>Assemblywoman, Marla Quintrell to discuss our<br>security issues</li>
    <li class="col-left" style="top:406px"><svg class="tick"><use href="#tick"/></svg>Focused on maintenance of streetlights to<br>make brighter streets</li>
    <li class="col-left" style="top:445px"><svg class="tick"><use href="#tick"/></svg>Negotiated Contract &amp; Hired Our New Land-<br>scaper, Oakhollow Landscapers</li>
    <li class="col-left" style="top:482.5px"><svg class="tick"><use href="#tick"/></svg>Major Homeowner Shrub Replacement Project</li>

    <li class="col-right" style="top:233px"><svg class="tick"><use href="#tick"/></svg>Addressing Standing Water in our Park<br>(Installed French Drain)</li>
    <li class="col-right" style="top:271.5px"><svg class="tick"><use href="#tick"/></svg>Replaced and upgraded all 5 outdoor circuit<br>breaker panels</li>
    <li class="col-right" style="top:310.5px"><svg class="tick"><use href="#tick"/></svg>Write monthly community newsletters</li>
    <li class="col-right" style="top:333px"><svg class="tick"><use href="#tick"/></svg>Sewer cleaning project (had all community<br>catch basins cleaned)</li>
    <li class="col-right" style="top:371.5px"><svg class="tick"><use href="#tick"/></svg>Carefully overseeing our new school project.</li>
    <li class="col-right" style="top:394px"><svg class="tick"><use href="#tick"/></svg>Coordinating with the sponsor and the school<br>directors</li>
    <li class="col-right" style="top:433px"><svg class="tick"><use href="#tick"/></svg>Delivered a very healthy budget<br>to the community</li>
    <li class="col-right" style="top:471.5px"><svg class="tick"><use href="#tick"/></svg>Works closely with our<br>committees</li>

    <li class="event-line" style="top:510px"><svg class="tick"><use href="#tick"/></svg><strong>Events:</strong> Zoo event, Petting Zoo, Outdoor Movie Night, Egg Hunt</li>
  </ul>

  <p class="intent">It is my intent to seek re-election.</p>
  <h2 class="candidate-name">DORIAN LINDQVIST</h2>
  <ul class="qualities">
    <li>Dedicated to improving our community</li>
    <li>Hard-working...He gets thing done!</li>
    <li>Trustworthy</li>
  </ul>
</main>
</body>
</html>
```